Bed and Breakfast WebSite Design

We need a webdesign for a bed and breakfast in Germany. This house is located at the scenic river Mosel in Germany, a very small town called Piesport. It's a region known for its wines. A lot of nature, bicycle routes, hiking, boat tours...

The house itself is a former monastery and because of that a listed, historic buildung.
The house is entirely renewed and has a very modern, individual interieur with "boutique hotel" style rooms. Every room is different. Its family owned and operated.

The website should find a bridge between historic charme and modern individual friendlyness. Very straight, not fancy. The website should express familiy friendlyness, modern comfort and emphasize that its place to RELAX.

In the attachment you'll find a lot of photos of house and surrounding. Theres a separate zip with quennabox stockphotos of that particular location/town (not purchased yet).

Number of Pages Required

1 page

Requirements
Must have
• Should be "easily" made responsive.

```html
<!DOCTYPE html>
<html lang="en">
<head>
<meta charset="utf-8">
<title>Talblick Inn – Bed &amp; Breakfast</title>
<link href="https://fonts.googleapis.com/css2?family=Space+Grotesk:wght@400;500;600;700&display=swap" rel="stylesheet">
<style>
:root{
  --ink:#111417;
  --dark:#0f1519;
  --orange:#e2552a;
  --grey:#f3f4f6;
  --band:#e6e7e9;
  --white:#ffffff;
  --muted:#3b3f44;
  --body:"Space Grotesk",sans-serif;
}
*{margin:0;padding:0;box-sizing:border-box}
html,body{width:1200px;height:4886px;overflow:hidden}
body{position:relative;font-family:var(--body);color:var(--ink);background:var(--white)}
.abs{position:absolute}
.photo{position:absolute}
.framed{border:3px solid var(--white)}
.txt{font-size:13px;line-height:27px;color:var(--muted)}
.on-dark{color:#e9ecef}
.btn{position:absolute;display:flex;align-items:center;justify-content:center;font-size:14px;font-weight:500}

/* hero */
.hero{position:absolute;left:0;top:0;width:1200px;height:686px;background:linear-gradient(180deg,#1d2630 0%,#2a3330 40%,#3f4a35 70%,#33402c 100%)}
.brand{left:112px;top:38px;display:flex;align-items:center;gap:10px;color:#fff;font-size:22px;font-weight:600}
.brand i{width:12px;height:12px;background:var(--orange)}
.nav{left:421px;top:40px;display:flex;gap:30px;color:#fff;font-size:13px}
.nav-line{left:421px;top:89px;width:667px;height:1px;background:rgba(255,255,255,.6)}
.book{left:957px;top:30px;width:131px;height:42px;background:#000;color:#fff;font-size:13px}
.eyebrow{left:0;width:1200px;top:214px;text-align:center;color:#fff;font-size:13px;font-weight:600}
.hero-title{left:0;width:1200px;top:232px;text-align:center;color:#fff;font-size:60px;font-weight:600;line-height:72px}
.hero-text{left:195px;width:810px;top:312px;text-align:center;color:#fff;font-size:14px;line-height:28px}
.hero-btn{left:508px;top:415px;width:184px;height:51px;border:2px solid #fff;color:#fff}
.dots{left:55px;top:278px;width:16px;display:flex;flex-direction:column;align-items:center;gap:4px;color:#fff}
.dots i{width:11px;height:11px;border:1.5px solid #fff;border-radius:50%}
.dots i.on{background:#fff}

/* about */
.about-side{left:603px;top:686px;width:597px;height:652px;background:var(--grey)}
.kicker{font-size:22px;font-weight:500}
.stat{width:160px;text-align:center}
.stat b{display:block;color:var(--orange);font-size:40px;font-weight:500}
.stat span{font-size:12px}

/* amenities */
.amen{left:0;top:1338px;width:1200px;height:719px;background:var(--dark)}
.amen-title{left:199px;top:1384px;color:#fff;font-size:40px;font-weight:600;line-height:50px}
.icon-cell{width:160px;text-align:center;color:#fff;font-size:13px;font-weight:500}
.icon-cell svg{display:block;margin:0 auto 8px}

/* rooms */
.section-title{left:0;width:1200px;text-align:center;font-size:40px;font-weight:500}
.room{position:absolute;width:297px}
.room .pic{height:273px;box-shadow:0 4px 10px rgba(0,0,0,.2)}
.room h3{font-size:14px;font-weight:600;margin:22px 0 6px}
.room p{font-size:12px;line-height:24px;color:var(--muted)}
.room a{display:block;margin-top:8px;font-size:13px;font-weight:600;color:var(--orange);text-decoration:underline}
.dark-btn{border:2px solid var(--ink);color:var(--ink)}

/* relax */
.relax{left:0;top:3282px;width:1200px;height:586px;background:var(--band)}
.relax-h{font-size:24px;font-weight:500}
.relax-h em{font-style:normal;color:var(--orange);font-size:36px}

/* contact & footer */
.footer{left:0;top:4290px;width:1200px;height:596px;background:linear-gradient(180deg,#1a2026,#12171b)}
.card{left:599px;top:3989px;width:370px;height:519px;background:#fff}
.pin{position:absolute;width:40px;height:40px;border-radius:50%;background:#fff;box-shadow:0 2px 10px rgba(0,0,0,.2);display:flex;align-items:center;justify-content:center}
.f-brand{left:0;width:1200px;top:4596px;text-align:center;color:#fff;font-size:46px;font-weight:600;line-height:56px}
.f-nav{left:0;width:1200px;top:4669px;display:flex;justify-content:center;gap:28px;color:#fff;font-size:14px}
.socials{left:0;width:1200px;top:4712px;display:flex;justify-content:center;gap:12px}
.socials span{width:40px;height:40px;border:1.5px solid #fff;border-radius:50%}
.copy{left:0;width:1200px;top:4782px;text-align:center;color:#fff;font-size:14px}
</style>
</head>
<body>

<!-- Hero -->
<section class="hero" role="img" aria-label="Evening view over vineyards and the winding river valley"></section>
<div class="abs brand"><i></i><span>Talblick Inn</span></div>
<nav class="abs nav"><span>Home</span><span>About Us</span><span>Our Rooms</span><span>Blog</span><span>Contact</span><span>Eng ⌄</span></nav>
<div class="abs nav-line"></div>
<div class="btn book">Book Now</div>
<div class="abs dots"><span>↑</span><i class="on"></i><i></i><i></i><i></i><i></i><span>↓</span></div>
<p class="abs eyebrow">LIVE THE EXPERIENCE</p>
<h1 class="abs hero-title">TALBLICK INN</h1>
<p class="abs hero-text">Lorem ipsum dolor sit amet, consectetur adipiscing elit, sed do eiusmod tempor incididunt ut labore et dolore magna aliqua. Ut enim ad minim veniam, quis nostrud exercitation ullamco laboris nisi ut aliquip ex ea commodo consequat. Duis aute irure dolor in reprehenderit in voluptate velit esse cillum</p>
<div class="btn hero-btn">View Our Rooms</div>

<!-- About -->
<div class="abs about-side"></div>
<div class="photo framed" style="left:660px;top:627px;width:478px;height:577px;background:linear-gradient(180deg,#8fb3d9 0%,#c9d8e6 35%,#4f6b3a 55%,#2f5a55 75%,#3a6f7a 100%)" role="img" aria-label="Historic house behind trees across a calm river"></div>
<div class="abs" style="left:112px;top:860px;display:flex;align-items:center;gap:6px"><span style="width:80px;height:2px;background:var(--ink)"></span><span class="kicker">About</span></div>
<h2 class="abs" style="left:110px;top:890px;color:var(--orange);font-size:40px;font-weight:500">Talblick Inn</h2>
<p class="abs txt" style="left:110px;top:955px;width:430px">Lorem ipsum dolor sit amet, consectetur adipiscing elit, sed do eiusmod tempor incididunt ut labore et dolore magna aliqua. Ut enim ad minim veniam, quis nostrud exercitation ullamco laboris nisi ut aliquip ex ea commodo consequat.</p>
<p class="abs txt" style="left:110px;top:1076px;width:430px">Lorem ipsum dolor sit amet, consectetur adipiscing elit, sed do eiusmod tempor incididunt ut labore et dolore magna aliqua. Ut enim ad minim veniam, quis nostrud</p>
<div class="abs stat" style="left:656px;top:1228px"><b>50</b><span>HOTEL ROOMS</span></div>
<div class="abs stat" style="left:819px;top:1228px"><b>10</b><span>ACTIVITIES</span></div>
<div class="abs stat" style="left:982px;top:1228px"><b>5</b><span>RESTAURANTS</span></div>

<!-- Amenities -->
<section class="abs amen"></section>
<div class="abs" style="left:112px;top:1412px;width:80px;height:2px;background:#fff"></div>
<h2 class="abs amen-title">OUR<br>AMENITIES</h2>
<div class="photo" style="left:9px;top:1502px;width:590px;height:413px;background:linear-gradient(160deg,#1d2a5a 0%,#2c3550 40%,#6a4a2a 65%,#22261f 100%)" role="img" aria-label="Lit terrace with parasols in front of the half-timbered house at dusk"></div>
<div class="photo framed" style="left:275px;top:1811px;width:292px;height:201px;background:linear-gradient(180deg,#8dbbe0 0%,#6f9d3e 40%,#4d7a2d 70%,#3d6a5a 100%)" role="img" aria-label="Green vineyard slopes above the river"></div>
<p class="abs txt on-dark" style="left:643px;top:1443px;width:430px">Lorem ipsum dolor sit amet, consectetur adipiscing elit, sed do eiusmod tempor incididunt ut labore et dolore magna aliqua. Ut enim ad minim veniam, quis nostrud exercitation ullamco laboris nisi ut aliquip ex ea commodo consequat.</p>
<p class="abs txt on-dark" style="left:643px;top:1562px;width:430px">Lorem ipsum dolor sit amet, consectetur adipiscing elit, sed do eiusmod tempor incididunt ut labore et dolore magna aliqua. Ut enim ad minim veniam, quis nostrud</p>

<div class="abs icon-cell" style="left:618px;top:1668px"><svg width="40" height="32" viewBox="0 0 40 32" fill="none" stroke="#fff" stroke-width="2"><rect x="4" y="9" width="5" height="14"/><rect x="31" y="9" width="5" height="14"/><line x1="9" y1="16" x2="31" y2="16"/><line x1="1" y1="16" x2="4" y2="16"/><line x1="36" y1="16" x2="39" y2="16"/></svg>FITNESS CENTER</div>
<div class="abs icon-cell" style="left:783px;top:1668px"><svg width="40" height="32" viewBox="0 0 40 32" fill="none" stroke="#fff" stroke-width="2"><rect x="4" y="16" width="32" height="12"/><path d="M8 16v-6h24v6M14 8c0-3 4-3 4-6M22 8c0-3 4-3 4-6"/></svg>JACUZZI</div>
<div class="abs icon-cell" style="left:951px;top:1668px"><svg width="40" height="32" viewBox="0 0 40 32" fill="none" stroke="#fff" stroke-width="2"><circle cx="20" cy="7" r="4"/><path d="M4 18c4-3 8 3 12 0s8 3 12 0 8 3 8 0M4 24c4-3 8 3 12 0s8 3 12 0 8 3 8 0"/></svg>SWIMMING POOL</div>
<div class="abs icon-cell" style="left:618px;top:1780px"><svg width="40" height="32" viewBox="0 0 40 32" fill="none" stroke="#fff" stroke-width="2"><circle cx="12" cy="8" r="4"/><rect x="4" y="16" width="32" height="6"/><path d="M8 22v8M32 22v8"/></svg>SPA TREATMENT</div>
<div class="abs icon-cell" style="left:783px;top:1780px"><svg width="40" height="32" viewBox="0 0 40 32" fill="none" stroke="#fff" stroke-width="2"><circle cx="11" cy="11" r="7"/><circle cx="29" cy="11" r="7"/><path d="M11 18v12M29 18v12M2 30h36"/></svg>GARDEN</div>
<div class="abs icon-cell" style="left:951px;top:1780px"><svg width="40" height="32" viewBox="0 0 40 32" fill="none" stroke="#fff" stroke-width="2"><rect x="4" y="12" width="9" height="18"/><rect x="15" y="4" width="10" height="26"/><rect x="27" y="16" width="9" height="14"/></svg>CITY VIEW</div>

<!-- Rooms -->
<h2 class="abs section-title" style="top:2140px">Our Rooms</h2>
<article class="room" style="left:133px;top:2218px"><div class="pic" style="background:linear-gradient(180deg,#5d7a5a 0%,#8a6a4a 45%,#e8e8ea 70%,#cfcfd2 100%)" role="img" aria-label="Double bed in front of a floral wallpaper wall"></div><h3>Lorem ipsum dolor</h3><p>Lorem ipsum dolor sit amet, consectetur adipiscing elit, sed do eiusmod tempor incididunt ut labore et</p><a>Book Now</a></article>
<article class="room" style="left:453px;top:2218px"><div class="pic" style="background:linear-gradient(180deg,#e6e2da 0%,#d8d2c6 40%,#3a3532 60%,#8a5a34 100%)" role="img" aria-label="Modern room with dark headboard and wall clock"></div><h3>Lorem ipsum dolor</h3><p>Lorem ipsum dolor sit amet, consectetur adipiscing elit, sed do eiusmod tempor incididunt ut labore et</p><a>Book Now</a></article>
<article class="room" style="left:772px;top:2218px"><div class="pic" style="background:linear-gradient(90deg,#efece6 0%,#d9d0c2 50%,#a9a095 100%)" role="img" aria-label="Bright room with patterned curtains and red chair"></div><h3>Lorem ipsum dolor</h3><p>Lorem ipsum dolor sit amet, consectetur adipiscing elit, sed do eiusmod tempor incididunt ut labore et</p><a>Book Now</a></article>
<article class="room" style="left:133px;top:2666px"><div class="pic" style="background:linear-gradient(180deg,#f0dcdc 0%,#e8c8c8 45%,#5a3a30 65%,#dcdcde 100%)" role="img" aria-label="Canopy bed in a pink room"></div><h3>Lorem ipsum dolor</h3><p>Lorem ipsum dolor sit amet, consectetur adipiscing elit, sed do eiusmod tempor incididunt ut labore et</p><a>Book Now</a></article>
<article class="room" style="left:453px;top:2666px"><div class="pic" style="background:linear-gradient(180deg,#6a4a34 0%,#e4e1da 40%,#d0ccc4 75%,#9a7a5a 100%)" role="img" aria-label="Twin room under exposed wooden beams"></div><h3>Lorem ipsum dolor</h3><p>Lorem ipsum dolor sit amet, consectetur adipiscing elit, sed do eiusmod tempor incididunt ut labore et</p><a>Book Now</a></article>
<article class="room" style="left:772px;top:2666px"><div class="pic" style="background:linear-gradient(180deg,#5a3c28 0%,#d8cfa8 40%,#c9b48a 70%,#8a6a48 100%)" role="img" aria-label="Attic room with beams and beige bedding"></div><h3>Lorem ipsum dolor</h3><p>Lorem ipsum dolor sit amet, consectetur adipiscing elit, sed do eiusmod tempor incididunt ut labore et</p><a>Book Now</a></article>
<div class="btn dark-btn" style="left:508px;top:3144px;width:184px;height:54px">View Our Rooms</div>

<!-- Relax -->
<section class="abs relax"></section>
<div class="photo" style="left:9px;top:3308px;width:590px;height:423px;background:linear-gradient(180deg,#8fb8de 0%,#4f7a34 35%,#3e6a2a 65%,#6d7278 100%)" role="img" aria-label="Garden terrace with parasol and lounge seating below green hills"></div>
<div class="photo framed" style="left:277px;top:3627px;width:290px;height:201px;background:linear-gradient(180deg,#5a8a3a 0%,#3f6a2a 50%,#6a5a3a 100%)" role="img" aria-label="Picnic table under trees in the garden"></div>
<div class="abs" style="left:643px;top:3423px;display:flex;align-items:center;gap:8px"><span style="width:42px;height:2px;background:var(--ink)"></span><span class="relax-h">Modern Comfort and Emphasize</span></div>
<p class="abs relax-h" style="left:693px;top:3456px">That its Place to <em>RELAX</em></p>
<p class="abs txt" style="left:643px;top:3518px;width:430px">Lorem ipsum dolor sit amet, consectetur adipiscing elit, sed do eiusmod tempor incididunt ut labore et dolore magna aliqua. Ut enim ad minim veniam, quis nostrud exercitation ullamco laboris nisi ut aliquip ex ea commodo consequat.</p>
<p class="abs txt" style="left:643px;top:3645px;width:430px">Lorem ipsum dolor sit amet, consectetur adipiscing elit, sed do eiusmod tempor incididunt ut labore et dolore magna aliqua. Ut enim ad minim veniam, quis nostrud</p>

<!-- Contact & footer -->
<footer class="abs footer"></footer>
<div class="photo" style="left:231px;top:3989px;width:368px;height:519px;background:linear-gradient(180deg,#6a8a4a 0%,#3e5a2a 35%,#2c2f30 60%,#6a4a30 100%)" role="img" aria-label="Rusty metal house sign beneath vineyard greenery"></div>
<div class="abs card"></div>
<h2 class="abs" style="left:643px;top:4046px;font-size:34px;font-weight:500">Contact Us</h2>
<div class="pin" style="left:640px;top:4100px"><svg width="12" height="16" viewBox="0 0 12 16"><path d="M6 0a6 6 0 0 0-6 6c0 4 6 10 6 10s6-6 6-10a6 6 0 0 0-6-6z" fill="#111"/><circle cx="6" cy="6" r="2" fill="#fff"/></svg></div>
<p class="abs" style="left:643px;top:4152px;font-size:14px;line-height:26px">Talblick Inn Inh. Greta Lindner<br>Lindenweg 12 •<br>54321 Talbach/Mosel</p>
<div class="pin" style="left:640px;top:4246px"><svg width="14" height="14" viewBox="0 0 24 24"><path d="M6 2l4 4-2 3c1 3 4 6 7 7l3-2 4 4-3 4C10 22 2 14 2 5z" fill="#111"/></svg></div>
<p class="abs" style="left:643px;top:4294px;font-size:14px;line-height:28px">Tell &nbsp;- &nbsp;49(0)6500 - 12 34 560 •<br>Mobil &nbsp;- &nbsp;+49(0)150 - 000 12 345</p>
<div class="pin" style="left:640px;top:4375px"><svg width="14" height="11" viewBox="0 0 14 11"><rect width="14" height="11" fill="#111"/><path d="M0 0l7 6 7-6" stroke="#fff" fill="none"/></svg></div>
<p class="abs" style="left:643px;top:4425px;font-size:14px">Email: stay@talblick-inn.example</p>

<p class="abs f-brand">Talblick Inn</p>
<nav class="abs f-nav"><span>Home</span><span>About Us</span><span>Our Rooms</span><span>Blog</span><span>Contact</span><span>Eng ⌄</span></nav>
<div class="abs socials" aria-label="Social links"><span></span><span></span><span></span><span></span><span></span></div>
<p class="abs copy">© 2022 All Rights Reserved | Privacy Policy</p>

</body>
</html>
```